Need Business Cards for my Business

email address: rkpmarlowhollowworks@vendrimail.com
web address: rkpmarlowhollowworks.net
Slogan: We offer various QVN licenses
Rowland K. Pemberly
Please stick with colors of Company Logo
would like the card to be more of the color example of the logo.
If you need PDF copy of logo email me at the above account.
Creative control rests with you.

Industry/Entity Type

Business

Contact Information for Business Card

I am a minimalist, but would like something to pop and stand out amongst other cards, make it memorable.

Font styles to use
Serif
Decorative
Script

```html
<!DOCTYPE html>
<html lang="en">
<head>
<meta charset="utf-8">
<title>Marlow Hollow Works – Business Cards</title>
<link rel="stylesheet" href="https://fonts.googleapis.com/css2?family=Source+Sans+3:wght@400;600;700&display=swap">
<style>
  :root {
    --page-bg: #d9dbde;
    --navy-top: #3a4c60;
    --navy-bottom: #2b3a4b;
    --card-white: #ffffff;
    --card-white-shade: #eef0f2;
    --accent-red: #e8453c;
    --accent-blue: #3f7fc4;
    --brand-blue: #2f5f9a;
    --text-grey: #4a4f57;
    --text-light: #e9eef4;
  }
  * { margin: 0; padding: 0; box-sizing: border-box; }
  html, body { width: 1200px; height: 900px; overflow: hidden; }
  body {
    background: var(--page-bg);
    font-family: "Source Sans 3", Arial, sans-serif;
    position: relative;
  }
  .card {
    position: absolute;
    width: 660px;
    height: 377px;
    border-radius: 4px;
    overflow: hidden;
    box-shadow: 0 6px 18px rgba(0,0,0,0.18);
  }
  .card-back {
    left: 170px; top: 50px;
    background: linear-gradient(160deg, var(--navy-top), var(--navy-bottom));
  }
  .card-front {
    left: 370px; top: 473px;
    background: linear-gradient(160deg, var(--card-white) 55%, var(--card-white-shade));
  }
  .accent-band { position: absolute; left: 0; bottom: 0; width: 100%; height: 30px; }

  .brand { display: flex; align-items: center; gap: 12px; }
  .brand-mark { width: 22px; height: 22px; }
  .brand-name { font-weight: 700; letter-spacing: 0.04em; text-transform: uppercase; }

  .card-back .brand { position: absolute; left: 200px; top: 150px; }
  .card-back .brand-mark { background: var(--accent-blue); }
  .card-back .brand-name { color: #ffffff; font-size: 30px; }
  .card-back .site {
    position: absolute; left: 0; right: 0; bottom: 58px;
    text-align: center; color: var(--text-light);
    font-size: 17px; letter-spacing: 0.22em;
  }

  .card-front .brand { position: absolute; right: 36px; top: 44px; }
  .card-front .brand-mark { background: var(--accent-red); }
  .card-front .brand-name { color: var(--brand-blue); font-size: 30px; }
  .card-front .slogan {
    position: absolute; right: 40px; top: 92px;
    color: var(--text-grey); font-size: 17px; letter-spacing: 0.1em;
  }
  .holder { position: absolute; left: 44px; top: 200px; }
  .holder-name { color: var(--accent-red); font-size: 24px; font-weight: 700; }
  .holder-rule { display: flex; margin: 10px 0 14px; }
  .holder-rule span { width: 28px; height: 4px; }
  .holder-rule .red { background: var(--accent-red); }
  .holder-rule .blue { background: var(--accent-blue); }
  .contact-list { list-style: none; }
  .contact-list li {
    display: flex; align-items: center; gap: 10px;
    color: var(--text-grey); font-size: 16px; line-height: 24px;
  }
  .contact-list svg { width: 13px; height: 13px; flex: none; }
</style>
</head>
<body>

<section class="card card-back">
  <div class="brand">
    <span class="brand-mark"></span>
    <span class="brand-name">Marlow Hollow Works</span>
  </div>
  <p class="site">www.rkpmarlowhollowworks.net</p>
  <svg class="accent-band" viewBox="0 0 660 30" preserveAspectRatio="none">
    <rect x="0" y="18" width="300" height="12" fill="var(--accent-red)"/>
    <polygon points="300,18 660,6 660,16 300,30" fill="var(--accent-blue)"/>
  </svg>
</section>

<section class="card card-front">
  <div class="brand">
    <span class="brand-mark"></span>
    <span class="brand-name">Marlow Hollow Works</span>
  </div>
  <p class="slogan">We offer various QVN licenses</p>

  <div class="holder">
    <h1 class="holder-name">Rowland K. Pemberly</h1>
    <div class="holder-rule"><span class="red"></span><span class="blue"></span></div>
    <ul class="contact-list">
      <li>
        <svg viewBox="0 0 16 16"><path d="M4 1l3 3-2 2c1 2 3 4 5 5l2-2 3 3-2 3C7 15 1 9 1 3z" fill="var(--accent-red)"/></svg>
        410-555-0186
      </li>
      <li>
        <svg viewBox="0 0 16 16"><rect x="1" y="3" width="14" height="10" rx="1" fill="var(--accent-red)"/><path d="M1 4l7 5 7-5" stroke="#fff" stroke-width="1.4" fill="none"/></svg>
        rkpmarlowhollowworks@vendrimail.com
      </li>
      <li>
        <svg viewBox="0 0 16 16"><circle cx="8" cy="8" r="7" fill="var(--accent-red)"/><path d="M1 8h14M8 1c-3 4-3 10 0 14M8 1c3 4 3 10 0 14" stroke="#fff" stroke-width="1" fill="none"/></svg>
        www.rkpmarlowhollowworks.net
      </li>
    </ul>
  </div>

  <svg class="accent-band" viewBox="0 0 660 30" preserveAspectRatio="none">
    <rect x="0" y="18" width="340" height="12" fill="var(--accent-red)"/>
    <polygon points="340,18 660,6 660,16 340,30" fill="var(--accent-blue)"/>
  </svg>
</section>

</body>
</html>
```